Brookmere Osteopathy and dry needling business card

Business card for Brookmere Osteopathy and Dry Needling.

Industry/Entity Type

Health

Contact Information for Business Card

I do not have a phone number yet. I also do not have an email address yet. The physical address is: 47 Lindcombe Lane Brookmere The website is: www.brookmereosteopathyclinic.example My details are: Dr Marcus Penhallow, Osteopath (B.Clin.Sci (Ost) M.Ost BSC ECON (Hons)

Colors
0094D4
00A9DD
6FCCEA
C7EBF8
E9F6FB

Requirements
Must have
• logo on the back
Nice to have
• Maybe a space for me to write an appointment time and date on the card.

```html
<!DOCTYPE html>
<html lang="en">
<head>
<meta charset="utf-8">
<title>Brookmere Osteopathy and Dry Needling – Business Card</title>
<link rel="stylesheet" href="https://fonts.googleapis.com/css2?family=Poppins:wght@300;400;500;600;700&display=swap">
<style>
  :root {
    --page-bg: #eceef1;
    --card-bg: #ffffff;
    --brand-blue: #1a86c8;
    --brand-orange: #ee8a1e;
    --text-grey: #4a4a4a;
    --faint-grey: #ececec;
  }
  * { box-sizing: border-box; margin: 0; padding: 0; }
  html, body {
    width: 1200px; height: 900px; overflow: hidden;
    background: var(--page-bg);
    font-family: "Poppins", sans-serif;
  }
  .canvas {
    width: 1200px; height: 900px;
    display: flex; align-items: center; justify-content: center; gap: 48px;
  }
  .card {
    position: relative;
    width: 520px; height: 300px;
    background: var(--card-bg);
    box-shadow: 0 10px 28px rgba(0,0,0,.12);
    overflow: hidden;
  }
  .card__decoration {
    position: absolute; left: -40px; bottom: -60px;
    width: 360px; height: 300px;
    background: radial-gradient(ellipse at 45% 55%, var(--faint-grey) 0%, rgba(236,236,236,.55) 45%, rgba(255,255,255,0) 72%);
  }
  .brand-seal {
    position: absolute; top: 22px; right: 26px;
    width: 118px; height: 118px;
    border: 2px solid var(--brand-blue); border-radius: 50%;
    display: flex; align-items: center; justify-content: center;
    text-align: center; padding: 14px;
  }
  .brand-seal__name {
    color: var(--brand-blue); font-weight: 500;
    font-size: 11px; line-height: 1.35; text-transform: uppercase; letter-spacing: .5px;
  }
  .practitioner { position: absolute; left: 30px; top: 150px; right: 24px; }
  .practitioner__name {
    color: var(--brand-blue); font-weight: 600; font-size: 19px; letter-spacing: .2px; line-height: 1.3;
  }
  .practitioner__role-row { display: flex; align-items: center; gap: 6px; margin-top: 1px; }
  .practitioner__role {
    color: var(--brand-orange); font-weight: 400; font-size: 10.5px; white-space: nowrap;
  }
  .rule { flex: 1; height: 1px; }
  .rule--orange { background: var(--brand-orange); }
  .rule--blue { background: var(--brand-blue); }
  .contact-list { position: absolute; left: 30px; top: 222px; list-style: none; }
  .contact-list__item {
    display: flex; align-items: center; gap: 8px;
    font-size: 11px; font-weight: 300; color: var(--text-grey);
  }
  .contact-list__icon { width: 12px; height: 12px; fill: var(--brand-blue); flex: none; }
  .address {
    position: absolute; right: 26px; top: 200px;
    text-align: right; font-size: 11.5px; font-weight: 300; font-style: normal;
    color: var(--text-grey); line-height: 1.4;
  }
  .appointment { position: absolute; left: 30px; right: 24px; top: 178px; }
  .appointment__title-row { display: flex; align-items: flex-end; gap: 6px; }
  .appointment__title { color: var(--brand-orange); font-weight: 700; font-size: 21px; white-space: nowrap; line-height: 1.3; }
  .appointment__title-row .rule { margin-bottom: 7px; }
  .appointment__field { display: flex; align-items: flex-end; gap: 8px; margin-top: 10px; }
  .appointment__label { color: var(--brand-blue); font-size: 14px; font-weight: 400; line-height: 1.3; }
  .appointment__field .rule { margin-bottom: 5px; }
</style>
</head>
<body>
<main class="canvas">

  <section class="card card--front">
    <div class="card__decoration" role="img" aria-label="Faint spine and sunrise illustration"></div>
    <div class="brand-seal"><span class="brand-seal__name">Brookmere Osteopathy and Dry Needling</span></div>

    <div class="practitioner">
      <h1 class="practitioner__name">Dr. MARCUS PENHALLOW</h1>
      <div class="practitioner__role-row">
        <p class="practitioner__role">Osteopath (B.Clin.Sci (Ost) M.Ost BSC ECON (Hons)</p>
        <span class="rule rule--orange"></span>
      </div>
    </div>

    <ul class="contact-list">
      <li class="contact-list__item">
        <svg class="contact-list__icon" viewBox="0 0 24 24"><path d="M12 2a10 10 0 1 0 0 20 10 10 0 0 0 0-20zm0 2c.9 1.2 1.6 2.6 2 4h-4c.4-1.4 1.1-2.8 2-4zM4.3 14a8 8 0 0 1 0-4h3.4a16 16 0 0 0 0 4zm.9 2h3c.3 1.3.8 2.6 1.5 3.7A8 8 0 0 1 5.2 16zm3-8h-3a8 8 0 0 1 4.5-3.7C9 5.4 8.5 6.7 8.2 8zM12 20c-.9-1.2-1.6-2.6-2-4h4c-.4 1.4-1.1 2.8-2 4zm2.3-6H9.7a14 14 0 0 1 0-4h4.6a14 14 0 0 1 0 4zm.1 5.7c.7-1.1 1.2-2.4 1.5-3.7h3a8 8 0 0 1-4.5 3.7zM16.3 14a16 16 0 0 0 0-4h3.4a8 8 0 0 1 0 4zm-.5-6c-.3-1.3-.8-2.6-1.5-3.7A8 8 0 0 1 18.8 8z"/></svg>
        www.brookmereosteopathyclinic.example
      </li>
    </ul>

    <address class="address">47 Lindcombe<br>Lane Brookmere</address>
  </section>

  <section class="card card--back">
    <div class="card__decoration" role="img" aria-label="Faint spine and sunrise illustration"></div>
    <div class="brand-seal"><span class="brand-seal__name">Brookmere Osteopathy and Dry Needling</span></div>

    <div class="appointment">
      <div class="appointment__title-row">
        <h2 class="appointment__title">Your Appointment</h2>
        <span class="rule rule--orange"></span>
      </div>
      <div class="appointment__field">
        <span class="appointment__label">Date</span>
        <span class="rule rule--blue"></span>
      </div>
      <div class="appointment__field">
        <span class="appointment__label">Time</span>
        <span class="rule rule--blue"></span>
      </div>
    </div>
  </section>

</main>
</body>
</html>
```